Business Card Design Project

for a second hand vintage clothing store. shop name is The Velvet Cupboard

Cards to be double sided

The name on the card is Joanna Whitfield

Information to put on card:

The Velvet Cupboard
Joanna Whitfield (no job title)
42/871 Dunmore St, Glenwick, Sydney, NSW, 2009.
Mobile: 0412 905 261
Email: thevelvetcupboard@mailbox.com.au
Web: www.thevelvetcupboard.com.au

Target Market(s)

Women looking at vintage clothing

Industry/Entity Type

Clothing

```html
<!DOCTYPE html>
<html lang="en">
<head>
<meta charset="utf-8">
<title>The Velvet Cupboard – Business Card</title>
<link rel="stylesheet" href="https://fonts.googleapis.com/css2?family=Anton&family=Tinos:wght@700&display=swap">
<style>
  :root {
    --page: #ffffff;
    --parchment-light: #d9cdb2;
    --parchment-mid: #b8a680;
    --parchment-dark: #8f7a52;
    --maroon: #5a2236;
    --scroll-taupe: #a89878;
    --cream: #ecdca3;
    --ink-shadow: rgba(40, 25, 15, 0.55);
  }
  * { margin: 0; padding: 0; box-sizing: border-box; }
  html, body {
    width: 1041px;
    height: 1200px;
    overflow: hidden;
    background: var(--page);
  }
  .card {
    position: absolute;
    left: 58px;
    width: 928px;
    height: 534px;
    overflow: hidden;
    background:
      radial-gradient(ellipse at 30% 60%, var(--parchment-light) 0%, var(--parchment-mid) 60%, var(--parchment-dark) 100%);
  }
  .card--front { top: 41px; }
  .card--back { top: 610px; }
  .ornament {
    position: absolute;
    inset: 0;
    width: 928px;
    height: 534px;
  }
  .text {
    position: absolute;
    font-family: "Tinos", "Times New Roman", serif;
    font-weight: 700;
    color: var(--maroon);
    white-space: nowrap;
  }
  .shop-name {
    left: 45px;
    top: 82px;
    font-size: 50px;
    color: var(--cream);
  }
  .person-name {
    position: absolute;
    left: 40px;
    top: 300px;
    font-family: "Anton", "Impact", sans-serif;
    font-size: 52px;
    line-height: 1;
    color: var(--cream);
    text-shadow: 2px 2px 3px var(--ink-shadow);
    white-space: nowrap;
  }
  .address {
    left: 42px;
    top: 374px;
    font-size: 31px;
    line-height: 32px;
  }
  .mobile {
    left: 44px;
    top: 448px;
    font-size: 31px;
  }
  .website {
    right: 50px;
    top: 306px;
    font-size: 39px;
  }
  .email {
    right: 82px;
    top: 362px;
    font-size: 23px;
  }
</style>
</head>
<body>
  <section class="card card--front">
    <svg class="ornament" viewBox="0 0 928 534" role="img" aria-label="Baroque scrollwork illustration in maroon and taupe over a harlequin diamond background">
      <defs>
        <linearGradient id="scrollFront" x1="0" y1="0" x2="1" y2="1">
          <stop offset="0" stop-color="#a89878"/>
          <stop offset="0.5" stop-color="#5a2236"/>
          <stop offset="1" stop-color="#6b3a3f"/>
        </linearGradient>
      </defs>
      <path d="M40 0 H928 V534 H700 C700 420 640 330 560 260 C520 225 470 200 420 190 C300 170 150 140 40 60 Z" fill="url(#scrollFront)" opacity="0.85"/>
    </svg>
    <p class="text shop-name">The Velvet Cupboard</p>
    <h1 class="person-name">Joanna Whitfield</h1>
    <p class="text address">42/871 Dunmore St, Glenwick,<br>Sydney, NSW, 2009</p>
    <p class="text mobile">Mobile: 0412 905 261</p>
  </section>

  <section class="card card--back">
    <svg class="ornament" viewBox="0 0 928 534" role="img" aria-label="Baroque scrollwork illustration in maroon and taupe over a harlequin diamond background">
      <defs>
        <linearGradient id="scrollBack" x1="0" y1="1" x2="1" y2="0">
          <stop offset="0" stop-color="#5a2236"/>
          <stop offset="0.45" stop-color="#6b3a3f"/>
          <stop offset="1" stop-color="#a89878"/>
        </linearGradient>
      </defs>
      <path d="M0 0 H928 V60 C840 110 760 230 640 240 C520 250 420 200 360 250 C300 300 300 420 250 534 H0 Z" fill="url(#scrollBack)" opacity="0.85"/>
    </svg>
    <p class="text website">www.thevelvetcupboard.com.au</p>
    <p class="text email">Email: thevelvetcupboard@mailbox.com.au</p>
  </section>
</body>
</html>
```